Full Service Outdoor Property Management Company

We are looking for a new and fresh business card design. My company has been in business for 26 years. Winter: We are a large snow and ice management company that does work for commercial, industrial and municipal clients. We have been named "Top 100 Snow Companies in the U.S." for numerous years. Summer: We provide complete landscape maintenance and landscape design and construction for both residential and commercial clients. We must incorporate our logo into card design as well as (in no particular order):
Employees name
Office: (417) 803-2765
Cell: (xxx) xxx-xxxx
brightfold.com
1879 Marigold, Inkster MI 48141
(Something about 26 + years in business as well as "Top 100 snow contractors as stated above)
Target Market(s)
Winter: Commercial, Industrial, Municipal
Summer: Residential and Commercial
Industry/Entity Type
Construction
Contact Information for Business Card
This is a little challenging as we are using one card for essentially two companies that target different customers from summer to winter. Perhaps the back side could be split in two or something to highlight the different services?? I'm open to any ideas!! Looking forward to seeing what you come up with!
Requirements
Must have
- Logo
- (in no particular order)
- Employees name
- Office: (417) 803-2765
- Cell: (xxx) xxx-xxxx
- brightfold.com
- 1879 Marigold, Inkster MI 48141
Nice to have
- Something about 26 + years in business
- "Top 100 Snow Contractors in the U.S."
Should not have
- Cheesy pictures of lawn mowers and snow plows

```html
<!DOCTYPE html>
<html lang="en">
<head>
<meta charset="utf-8">
<title>Brightfold business card</title>
<link rel="stylesheet" href="https://fonts.googleapis.com/css2?family=Tinos:wght@400;700&family=PT+Sans&display=swap">
<style>
  :root {
    --backdrop: #8dc63f;
    --brand-green: #0b7f48;
    --brand-blue: #3a87c8;
    --paper: #ffffff;
    --edge: #5a5a5a;
  }
  * { margin: 0; padding: 0; box-sizing: border-box; }
  html, body { width: 1200px; height: 1141px; overflow: hidden; }
  body {
    position: relative;
    background: var(--backdrop);
    border: 1px solid #4d6b2a;
    font-family: "PT Sans", sans-serif;
  }
  .card {
    position: absolute;
    width: 881px;
    height: 501px;
    background: var(--paper);
    border: 1px solid var(--edge);
    overflow: hidden;
  }
  .card--front { left: 276px; top: 48px; }
  .card--back { left: 55px; top: 575px; }
  .card__shape { position: absolute; inset: 0; width: 100%; height: 100%; }
  .wordmark {
    position: absolute;
    left: 0; right: 0;
    text-align: center;
    font-family: "Tinos", serif;
    font-weight: 700;
    font-size: 72px;
    line-height: 1;
    color: var(--brand-green);
  }
  .card--front .wordmark { top: 80px; }
  .card--back .wordmark { top: 134px; }
  .holder {
    position: absolute;
    left: 0; width: 888px;
    text-align: center;
    color: var(--paper);
    font-family: "Tinos", serif;
  }
  .holder__name { top: 310px; font-weight: 700; font-size: 27px; }
  .holder__title { top: 348px; font-size: 19px; letter-spacing: 0.5px; }
  .contact {
    position: absolute;
    left: 0; width: 888px;
    display: flex;
    justify-content: center;
    gap: 14px;
    color: var(--paper);
    font-size: 20px;
    line-height: 1;
  }
  .contact--phones { top: 393px; }
  .contact--web { top: 425px; }
  .contact--address { top: 467px; }
  .contact__item { display: flex; align-items: center; gap: 7px; }
  .contact__icon { width: 16px; height: 16px; fill: var(--paper); }
  .credentials {
    position: absolute;
    left: 0; right: 0;
    top: 322px;
    text-align: center;
    font-family: "Tinos", serif;
    font-size: 23px;
    line-height: 41px;
    color: var(--brand-green);
  }
</style>
</head>
<body>

<section class="card card--front">
  <svg class="card__shape" viewBox="0 0 609 347" preserveAspectRatio="none" aria-hidden="true">
    <polygon points="78,263 304,166 530,262 304,174" fill="var(--brand-blue)"/>
    <polygon points="0,297 304,180 609,299 609,347 0,347" fill="var(--brand-green)"/>
  </svg>
  <div class="wordmark">Brightfold</div>
  <div class="holder holder__name">YOUR NAME</div>
  <div class="holder holder__title">TITLE</div>

  <div class="contact contact--phones">
    <span class="contact__item">
      <svg class="contact__icon" viewBox="0 0 16 16"><path d="M3.5 1l2.5 3-1.5 1.8c.8 2 2.7 3.9 4.7 4.7L11 9l3 2.5-1.3 2.7C7.2 14 2 8.8 1.8 3.3z"/></svg>
      123-456-7890
    </span>
    <span class="contact__item">
      <svg class="contact__icon" viewBox="0 0 16 16"><path d="M4 1h8v14H4zM5.5 3v8h5V3zM7 12.5h2v1.2H7z" fill-rule="evenodd"/></svg>
      123-456-7890
    </span>
  </div>

  <div class="contact contact--web">
    <span class="contact__item">
      <svg class="contact__icon" viewBox="0 0 16 16"><path d="M1 4h14v9H1zM2 5l6 4.5L14 5v1L8 10.5 2 6z" fill-rule="evenodd"/></svg>
      info@brightfold.com
    </span>
    <span class="contact__item">
      <svg class="contact__icon" viewBox="0 0 16 16"><path d="M8 1a7 7 0 100 14A7 7 0 008 1zm0 1.5c.9 1 1.5 2.7 1.7 4.7H6.3C6.5 5.2 7.1 3.5 8 2.5zM2.6 7.2a5.5 5.5 0 012.8-4.2c-.6 1.1-1 2.6-1.1 4.2zm0 1.6h1.7c.1 1.6.5 3.1 1.1 4.2a5.5 5.5 0 01-2.8-4.2zM8 13.5c-.9-1-1.5-2.7-1.7-4.7h3.4c-.2 2-.8 3.7-1.7 4.7zm2.6-.5c.6-1.1 1-2.6 1.1-4.2h1.7a5.5 5.5 0 01-2.8 4.2zm1.1-5.8c-.1-1.6-.5-3.1-1.1-4.2a5.5 5.5 0 012.8 4.2z"/></svg>
      www.brightfold.com
    </span>
  </div>

  <div class="contact contact--address">
    <span class="contact__item">
      <svg class="contact__icon" viewBox="0 0 16 16"><path d="M8 1a5 5 0 00-5 5c0 3.8 5 9 5 9s5-5.2 5-9a5 5 0 00-5-5zm0 7a2 2 0 110-4 2 2 0 010 4z"/></svg>
      1879 Marigold, Dunmore I 49302
    </span>
  </div>
</section>

<section class="card card--back">
  <div class="wordmark">Brightfold</div>
  <p class="credentials">
    Something About 26 + Years In Business<br>
    Top 100 Snow Contractors In The U.S.
  </p>
</section>

</body>
</html>
```